App-Design für Vergleichsportal für Reparaturen
Zielgruppe
Flickwerkstatt ist das Vergleichsportal für Reparaturen in deiner Nähe. Egal ob du eine Werkstatt für dein Smartphone, Tablet, Laptop, Computer, Smartwatch oder Spielkonsole suchst. Mit uns findest du deine passende Reparaturwerkstat in deiner Nähe mit dem besten Preis für dich. Du kannst dich direkt über unser Portal deinen Reparaturauftrag erhalten und wirst durch unser Sicher Kaufen Käuferschutz und unser MONVIRA Treuhandschutz abgesichert.
Aufgabenstellung
Unter Flickwerkstatt.de kann das aktuelle Design angeschaut werden. Die Farbe sollten übernommen werden.
Über die Startseite kann der Kunde sein Gerät, Service sowie seine Adresse eingeben. Auf der Vergleichsseite bekommt der Kunde die Übersicht welche Reparaturwerkstätten es gibt, zu welche Preisen die ausgewählte Dienstleistung angeboten wird. Wenn der Kunde auf den Button 'Jetzt Online Bestpreis buchen' drückt, dann kommt der Kunde in den Warenkorb. Im Warenkorb können noch weitere Dienstleistungen und Produkte dazugebucht werden. Und anschließend kommt der Kunde in die Kasse und kann der Bestellvorgang beenden. Die Benutzerführung sollte einfach sein. Im Fokus steht die Vergleichsseite. Dort sollte der Kunde ca. 4 Werkstätten auf einen Blick sehen können. Könnte ausschauen wie bei Wahlblick9 in der Kategorie Mobilfunk.
Die Vergleichseite sollte auf jeden Fall folgende Elemente enthalten:
- Entfernung zur Werkstatt in Meter bzw. Kilometer
- Logo der Werkstatt
- Name der Werkstatt
- Bewertungssterne der Werkstatt
- Reparaturzeit und Ersatzeilverfügbarkeit
- Reparaturpreis (Platz sollte auch bei Auswahl von 2 Dienstleistungen vorhanden sein)
- Rabattanzeige
- Qualitätssiegel (noch nicht vorhanden)
- Anzeige von Verknappung (z. B. noch 3 Termin frei)
- Qualitätsmerkmale (z. B. 12 Monate Garantie)
Die Merkmale Öffnungszeiten, Adresse, Kostenpflichtige Zusatzleistungen können aus Platzgründen in den Warenkorbseite wandern außer es gibt eine schöne und einfache Lösung.
In der Warenkorbseite kann dazu auch die Wahlblick9 Seite dienen.
Bei allen sollte auf die Benutzerfreundlichkeit geachtet werden.
Bei offenen Frage stehe ich zur Verfügung und freue mich auf viele Designs.
Vielen DANK im Voraus!

```html
<!DOCTYPE html>
<html lang="de">
<head>
<meta charset="utf-8">
<title>Flickwerkstatt – Startseite Mobil</title>
<link rel="stylesheet" href="https://fonts.googleapis.com/css2?family=Source+Sans+3:wght@300;400;600;700&display=swap">
<style>
  :root {
    --stage: #2a2b2c;
    --white: #ffffff;
    --field-bg: #f1f2f3;
    --navy: #234a5d;
    --green: #8bbd3a;
    --green-bright: #9acc3f;
    --text: #3c4a52;
    --placeholder: #a9b1b6;
    --red: #d8232a;
  }
  * { box-sizing: border-box; margin: 0; padding: 0; }
  html, body {
    width: 1200px; height: 728px; overflow: hidden;
    background: var(--stage);
    font-family: "Source Sans 3", "Myriad Pro", sans-serif;
  }
  .screen {
    position: absolute; left: 439px; top: 16px;
    width: 322px; height: 695px;
    background: var(--field-bg);
    overflow: hidden;
  }
  .app-header {
    position: absolute; left: 0; top: 0; width: 100%; height: 70px;
    background: var(--white);
  }
  .status-time {
    position: absolute; left: 16px; top: 6px;
    font-size: 12px; font-weight: 600; color: var(--text); letter-spacing: .3px;
  }
  .status-icons { position: absolute; right: 10px; top: 8px; }
  .brand {
    position: absolute; left: 12px; top: 38px;
    display: flex; align-items: center; gap: 5px;
    font-size: 13px; font-weight: 400; color: var(--navy);
  }
  .brand-dot { width: 9px; height: 9px; border-radius: 50%; background: var(--green); }
  .menu-toggle { position: absolute; right: 13px; top: 40px; }
  .hero {
    position: absolute; left: 0; top: 70px; width: 100%; height: 70px;
    background: var(--navy); text-align: center; color: var(--green-bright);
  }
  .hero-title { margin-top: 21px; font-size: 10.5px; font-weight: 700; }
  .hero-sub { margin-top: 2px; font-size: 8px; font-weight: 400; }
  .field {
    position: absolute; left: 25px; width: 271px; height: 39px;
    background: var(--white);
    display: flex; align-items: center; justify-content: space-between;
    padding: 0 10px; font-size: 12.5px; font-weight: 300; color: var(--text);
  }
  .field.placeholder { color: var(--placeholder); }
  .field .plus { color: var(--green); font-size: 13px; font-weight: 300; }
  .service-tag {
    position: absolute; left: 31px; top: 415px; width: 258px; height: 23px;
    background: var(--green); color: var(--white);
    display: flex; align-items: center; padding: 0 7px; gap: 6px;
    font-size: 9px; font-weight: 300;
  }
  .service-tag .tag-actions { margin-left: auto; display: flex; gap: 5px; }
  .cta {
    position: absolute; left: 25px; top: 523px; width: 271px; height: 39px;
    background: var(--navy); color: var(--white);
    display: flex; align-items: center; justify-content: center;
    font-size: 9.8px; font-weight: 400; letter-spacing: .1px;
  }
  .trust {
    position: absolute; top: 594px; width: 70px; text-align: center;
    font-size: 6.5px; color: var(--navy);
  }
  .trust svg { display: block; margin: 0 auto 5px; }
</style>
</head>
<body>
<main class="screen">
  <header class="app-header">
    <span class="status-time">9:41</span>
    <svg class="status-icons" width="54" height="10" viewBox="0 0 54 10">
      <rect x="0" y="6" width="2" height="3" fill="#3c4a52"/>
      <rect x="3" y="4.5" width="2" height="4.5" fill="#3c4a52"/>
      <rect x="6" y="3" width="2" height="6" fill="#3c4a52"/>
      <rect x="9" y="1" width="2" height="8" fill="#3c4a52"/>
      <path d="M16 3.5a7 7 0 0 1 10 0M18 5.5a4 4 0 0 1 6 0" stroke="#3c4a52" stroke-width="1.4" fill="none"/>
      <circle cx="21" cy="7.8" r="1.2" fill="#3c4a52"/>
      <rect x="33" y="1" width="17" height="8" rx="2" fill="none" stroke="#3c4a52"/>
      <rect x="34.5" y="2.5" width="14" height="5" rx="1" fill="#3c4a52"/>
      <rect x="51" y="3.5" width="1.5" height="3" fill="#3c4a52"/>
    </svg>
    <div class="brand"><span class="brand-dot"></span>Flickwerkstatt</div>
    <svg class="menu-toggle" width="20" height="14" viewBox="0 0 20 14">
      <path d="M0 1h20M0 7h20M0 13h20" stroke="#3c4a52" stroke-width="1.3"/>
    </svg>
  </header>

  <section class="hero">
    <p class="hero-title">Reparaturen Im Vergleich, in deiner Nähe!</p>
    <p class="hero-sub">Garantiert die besten Tarife</p>
  </section>

  <div class="field" style="top:172px">Reparaturkategorie wählen
    <svg width="8" height="5" viewBox="0 0 8 5"><path d="M.5.5 4 4 7.5.5" stroke="#8bbd3a" fill="none"/></svg></div>
  <div class="field" style="top:235px">Hersteller wählen
    <svg width="8" height="5" viewBox="0 0 8 5"><path d="M.5.5 4 4 7.5.5" stroke="#8bbd3a" fill="none"/></svg></div>
  <div class="field" style="top:298px">Gerät wählen
    <svg width="8" height="5" viewBox="0 0 8 5"><path d="M.5.5 4 4 7.5.5" stroke="#8bbd3a" fill="none"/></svg></div>
  <div class="field" style="top:362px">Dienstleistung wählen <span class="plus">+</span></div>

  <div class="service-tag">
    <svg width="8" height="12" viewBox="0 0 8 12"><rect x=".6" y=".6" width="6.8" height="10.8" rx="1.2" fill="none" stroke="#fff"/><path d="M3 10h2" stroke="#fff"/></svg>
    Display Original-Qualität
    <span class="tag-actions">
      <svg width="9" height="9" viewBox="0 0 9 9"><circle cx="4.5" cy="4.5" r="4.5" fill="#234a5d"/><path d="M4.5 4v3" stroke="#fff"/><circle cx="4.5" cy="2.5" r=".7" fill="#fff"/></svg>
      <svg width="9" height="9" viewBox="0 0 9 9"><circle cx="4.5" cy="4.5" r="4.5" fill="#d8232a"/><path d="M2.3 4.5h4.4" stroke="#fff" stroke-width="1.2"/></svg>
    </span>
  </div>

  <div class="field placeholder" style="top:459px; width:174px">Strasse eingeben</div>
  <div class="field placeholder" style="top:459px; left:212px; width:84px">Hausnr.</div>

  <div class="cta">AUF ZUM REPARATURWERKSTATTVERGLEICH &gt;</div>

  <div class="trust" style="left:31px">
    <svg width="46" height="54" viewBox="0 0 46 54">
      <path d="M23 2 43 9v19c0 12-9 20-20 24C12 48 3 40 3 28V9Z" fill="none" stroke="#8bbd3a" stroke-width="3"/>
      <path d="M23 8 38 13v15c0 9-7 16-15 19C15 44 8 37 8 28V13Z" fill="none" stroke="#234a5d" stroke-width="1"/>
      <text x="23" y="35" text-anchor="middle" font-size="20" fill="#234a5d" font-family="Source Sans 3, sans-serif">€</text>
    </svg>Käuferschutz
  </div>
  <div class="trust" style="left:125px">
    <svg width="46" height="54" viewBox="0 0 46 54">
      <path d="M23 2 43 9v19c0 12-9 20-20 24C12 48 3 40 3 28V9Z" fill="none" stroke="#8bbd3a" stroke-width="3"/>
      <path d="M23 8 38 13v15c0 9-7 16-15 19C15 44 8 37 8 28V13Z" fill="none" stroke="#234a5d" stroke-width="1"/>
      <path d="M13 27l6-6 4 2 4-2 6 6-8 7-4-3Z" fill="none" stroke="#234a5d" stroke-width="1.2" stroke-linejoin="round"/>
    </svg>Treuhandschutz
  </div>
  <div class="trust" style="left:219px">
    <svg width="46" height="54" viewBox="0 0 46 54">
      <path d="M23 2 43 9v19c0 12-9 20-20 24C12 48 3 40 3 28V9Z" fill="none" stroke="#8bbd3a" stroke-width="3"/>
      <path d="M23 8 38 13v15c0 9-7 16-15 19C15 44 8 37 8 28V13Z" fill="none" stroke="#234a5d" stroke-width="1"/>
      <path d="M18 24v-3a5 5 0 0 1 10 0v3" fill="none" stroke="#234a5d" stroke-width="1.2"/>
      <rect x="15.5" y="24" width="15" height="11" rx="2" fill="none" stroke="#234a5d" stroke-width="1.2"/>
      <circle cx="23" cy="29" r="1.5" fill="#234a5d"/>
    </svg>Datenschutz
  </div>
</main>
</body>
</html>
```